Kveldbrá - Start-up company selling electricity

Hello let me tell you about Kveldbrá.

Kveldbrá is start-up company selling electricity in Iceland. The operations of the company consist of making power usage forecasts for our customers, purchasing the electricity wholesale from the energy producers, and selling the electricity to the consumer. We are focused on tech by using optimization and machine learning to minimize electricity prices to our customers. Our marketing strategy is to portray a tech company mindset and to show dedication to driving down the electricity price on the market.

We need your help to make our website pop. Possible concepts to work with are as follows:

- Iceland the land of ice and fire
- Green energy
- Innovation
- Tech and data science

Link to our website: https://prufa.kveldbra.is/
We are open to ideas.
Thank you!

Target Market(s)

Electricity consumers both homes and companies.

Number of Pages Required

1 page

Font styles to use
Serif
Sans Serif

```html
<!DOCTYPE html>
<html lang="is">
<head>
<meta charset="utf-8">
<title>Kveldbrá – Sama rafmagn, bara ódýrara</title>
<link href="https://fonts.googleapis.com/css2?family=Noto+Sans:wght@400;600;700&display=swap" rel="stylesheet">
<style>
  :root {
    --page-bg: #ffffff;
    --brand-blue: #14a5dc;
    --band-light: #3bb5e3;
    --divider: rgba(255, 255, 255, 0.18);
    --white: #ffffff;
  }
  * { box-sizing: border-box; margin: 0; padding: 0; }
  html, body {
    width: 1200px;
    height: 849px;
    overflow: hidden;
    background: var(--page-bg);
    font-family: "Noto Sans", sans-serif;
  }
  .site {
    position: absolute;
    left: 0;
    top: 87px;
    width: 1200px;
    height: 674px;
    background: var(--brand-blue);
    overflow: hidden;
    color: var(--white);
  }
  .site-header {
    position: absolute;
    left: 0;
    top: 0;
    width: 100%;
    height: 76px;
    border-bottom: 1px solid var(--divider);
    display: flex;
    align-items: center;
    justify-content: space-between;
    padding: 0 19px;
  }
  .brand {
    display: flex;
    align-items: center;
    gap: 8px;
    font-size: 25px;
    font-weight: 600;
    letter-spacing: -0.2px;
  }
  .brand-dot {
    width: 18px;
    height: 18px;
    border-radius: 50%;
    background: var(--white);
  }
  .main-nav {
    display: flex;
    gap: 63px;
    font-size: 13px;
    font-weight: 700;
    letter-spacing: 0.5px;
    padding-top: 3px;
  }
  .main-nav a { color: var(--white); text-decoration: none; }
  .hero {
    position: absolute;
    inset: 0;
    text-align: center;
  }
  .hero-title {
    position: absolute;
    left: 0;
    width: 100%;
    top: 284px;
    font-size: 36px;
    font-weight: 700;
    letter-spacing: 1.4px;
  }
  .hero-lead {
    position: absolute;
    left: 0;
    width: 100%;
    top: 357px;
    font-size: 13.5px;
    font-weight: 400;
    line-height: 22px;
    letter-spacing: 0.9px;
  }
  .audience-buttons {
    position: absolute;
    left: 525px;
    top: 434px;
    display: flex;
    flex-direction: column;
    gap: 18px;
  }
  .audience-button {
    display: flex;
    align-items: center;
    justify-content: center;
    width: 149px;
    height: 42px;
    border-radius: 21px;
    background: var(--white);
    color: var(--brand-blue);
    font-size: 14px;
    letter-spacing: 0.8px;
    text-decoration: none;
    box-shadow: 0 3px 6px rgba(0, 60, 100, 0.18);
  }
  .footer-band {
    position: absolute;
    left: 0;
    bottom: 0;
    width: 100%;
    height: 80px;
    background: linear-gradient(to bottom, rgba(59, 181, 227, 0) 0%, var(--band-light) 100%);
  }
</style>
</head>
<body>
  <div class="site">
    <header class="site-header">
      <div class="brand"><span class="brand-dot"></span>Kveldbrá</div>
      <nav class="main-nav">
        <a href="#">Um Kveldbrá</a>
        <a href="#">Spurt &amp; Svarað</a>
        <a href="#">Viðskiptaskilmálar</a>
      </nav>
    </header>

    <section class="hero">
      <h1 class="hero-title">Sama rafmagn ~ Bara ódýrara!</h1>
      <p class="hero-lead">Kveldbrá notar gervigreind, gagnavísindi og sjálfvirkni til að<br>lágmarka kostnað og stuðla að okrujöfnuði</p>
      <div class="audience-buttons">
        <a class="audience-button" href="#">Fyrirtæki</a>
        <a class="audience-button" href="#">Heimili</a>
      </div>
    </section>

    <div class="footer-band" role="img" aria-label="Soft light-blue decorative band along the bottom edge"></div>
  </div>
</body>
</html>
```